Summit Guest Partners

An Editable Business Card Template For SGP & SGH
Similar or Different Design

418 W. Marlow Ridge Pkwy.
Suite 2230
Irving, TX 75038

```html
<!DOCTYPE html>
<html lang="en">
<head>
<meta charset="utf-8">
<title>Summit Guest Partners – Business Card</title>
<link href="https://fonts.googleapis.com/css2?family=Roboto+Slab:wght@400;700&family=Lato:wght@300;400&family=Roboto:wght@700&display=swap" rel="stylesheet">
<style>
  :root{
    --stage:#8f8f8f;
    --paper:#ffffff;
    --brand:#8e1a1d;
    --brand-light:#d0614f;
    --ink:#111111;
    --body:#444444;
    --rule:#222222;
  }
  *{margin:0;padding:0;box-sizing:border-box}
  html,body{width:1200px;height:1200px;overflow:hidden;background:var(--stage)}
  .card{position:absolute;left:269px;width:663px;height:380px;background:var(--paper);
        box-shadow:0 3px 6px rgba(0,0,0,.35);overflow:hidden;font-family:'Lato',sans-serif}
  .card--front{top:180px}
  .card--back{top:630px}
  .wave{position:absolute;left:0;bottom:0;width:663px;height:90px}
  .slab{font-family:'Roboto Slab',serif;font-weight:700}
  .abs{position:absolute;white-space:nowrap}

  .wordmark{text-align:center;font-family:'Roboto Slab',serif;font-weight:700;color:var(--brand);font-size:24px;line-height:1.15}

  .person__name{left:42px;top:138px;font-size:28px;color:var(--ink);letter-spacing:.5px}
  .person__role{left:41px;top:170px;font-size:19px;color:var(--brand)}
  .divider{left:42px;top:202px;width:583px;height:2px;background:var(--rule)}
  .contacts{left:41px;top:216px;font-size:17px;color:var(--body);line-height:21px}
  .contacts li{list-style:none;display:flex;align-items:center;gap:9px}
  .contacts svg{width:13px;height:13px;fill:var(--brand)}
  .address{right:38px;top:215px;text-align:right;font-size:17px;color:var(--body);line-height:22px}
  .tagline{left:71px;top:334px;font-size:25px;color:#fff}

  .headline{left:39px;top:42px;font-size:26px;line-height:26px;color:var(--brand)}
  .features{left:39px;top:130px;font-size:16px;color:var(--body);line-height:26px;font-weight:400}
  .features li{list-style:none;display:flex;align-items:center;gap:12px}
  .features li.cont{padding-left:28px}
  .features svg{width:16px;height:14px;flex:none}
  .office__label{right:50px;top:207px;font-family:'Roboto',sans-serif;font-weight:700;font-size:18px;color:var(--ink)}
  .office__phone{right:50px;top:225px;font-family:'Roboto',sans-serif;font-weight:700;font-size:36px;color:var(--brand)}
  .office__addr{right:50px;top:264px;font-size:12px;color:var(--ink)}
  .website{left:101px;top:330px;font-size:27px;color:#fff}
</style>
</head>
<body>

<section class="card card--front">
  <div class="abs wordmark" style="left:430px;top:72px;width:190px">Summit Guest<br>Housing</div>
  <div class="abs slab person__name">DANA WHITCOMBE</div>
  <div class="abs person__role">Sales Manager</div>
  <div class="abs divider"></div>
  <ul class="abs contacts">
    <li><svg viewBox="0 0 24 24"><path d="M6.6 10.8a15 15 0 0 0 6.6 6.6l2.2-2.2c.3-.3.7-.4 1-.2 1.1.4 2.3.6 3.6.6.6 0 1 .4 1 1V20c0 .6-.4 1-1 1A17 17 0 0 1 3 4c0-.6.4-1 1-1h3.5c.6 0 1 .4 1 1 0 1.3.2 2.5.6 3.6.1.3 0 .7-.2 1z"/></svg>214-555-0148</li>
    <li><svg viewBox="0 0 24 24"><path d="M7 1h10a2 2 0 0 1 2 2v18a2 2 0 0 1-2 2H7a2 2 0 0 1-2-2V3a2 2 0 0 1 2-2zm0 3v14h10V4z"/></svg>480-555-0193</li>
    <li><svg viewBox="0 0 24 24"><path d="M2 5h20v14H2zm2 2v.5l8 5 8-5V7z"/></svg>DWhitcombe@summitguest.com</li>
  </ul>
  <div class="abs address">418 W. Marlow Ridge Pkwy.<br>Suite 2230<br>Irving, TX 75038</div>
  <svg class="wave" viewBox="0 0 663 90" preserveAspectRatio="none" aria-hidden="true">
    <path d="M0 62 C90 10 200 0 300 6 C430 14 560 40 663 12 L663 20 C560 48 430 24 300 18 C200 14 90 24 0 66Z" fill="var(--brand-light)"/>
    <path d="M0 70 C90 26 200 16 300 20 C430 26 560 52 663 22 L663 90 L0 90Z" fill="var(--brand)"/>
  </svg>
  <div class="abs slab tagline">Oil Field Housing on Autopilot</div>
</section>

<section class="card card--back">
  <div class="abs slab headline">Experienced Provider<br>To Oil, Gas, Energy &amp;<br>Construction Industries</div>
  <ul class="abs features">
    <li><svg viewBox="0 0 16 14"><path d="M1 7.5 L6 12 L15 2" fill="none" stroke="var(--brand)" stroke-width="2.4" stroke-linecap="round" stroke-linejoin="round"/></svg>Consolidated Billing</li>
    <li><svg viewBox="0 0 16 14"><path d="M1 7.5 L6 12 L15 2" fill="none" stroke="var(--brand)" stroke-width="2.4" stroke-linecap="round" stroke-linejoin="round"/></svg>Full Service Corporate Lodging</li>
    <li><svg viewBox="0 0 16 14"><path d="M1 7.5 L6 12 L15 2" fill="none" stroke="var(--brand)" stroke-width="2.4" stroke-linecap="round" stroke-linejoin="round"/></svg>Live Customer Support 24/7/365</li>
    <li><svg viewBox="0 0 16 14"><path d="M1 7.5 L6 12 L15 2" fill="none" stroke="var(--brand)" stroke-width="2.4" stroke-linecap="round" stroke-linejoin="round"/></svg>Proven Track Record Of Performance</li>
    <li><svg viewBox="0 0 16 14"><path d="M1 7.5 L6 12 L15 2" fill="none" stroke="var(--brand)" stroke-width="2.4" stroke-linecap="round" stroke-linejoin="round"/></svg>Best Negotiated Rates &amp;</li>
    <li class="cont">No Additional Fees</li>
  </ul>
  <div class="abs wordmark" style="left:410px;top:85px;width:200px">Summit Guest<br>Partners</div>
  <div class="abs office__label">CORPORATE OFFICE</div>
  <div class="abs office__phone">214-555-0148</div>
  <div class="abs office__addr">77 North Elm Road Carlsbad, NM 88220</div>
  <svg class="wave" viewBox="0 0 663 90" preserveAspectRatio="none" aria-hidden="true">
    <path d="M0 62 C90 10 200 0 300 6 C430 14 560 40 663 12 L663 20 C560 48 430 24 300 18 C200 14 90 24 0 66Z" fill="var(--brand-light)"/>
    <path d="M0 70 C90 26 200 16 300 20 C430 26 560 52 663 22 L663 90 L0 90Z" fill="var(--brand)"/>
  </svg>
  <div class="abs slab website">www.SGPFieldStay.com</div>
</section>

</body>
</html>
```